Awesome Redesign of Plumbing website

A great website designer to create this page for us in Wordpress with elementor.

- You are redesigning this site: http://fjellbekkror.no/

- Brand name is : Vannlinje Nord

- You can take pictures from the website or the one i attach, or stock images or AI generated images etc.

- The main call to action is to call the phone number (+47 23 86 51 94)
So please make that a priority.
- Mobile responsiveness is very important.
- The background should be white. You can use the color code red, white and black when you create the site.

I want you to build the website with a high speed score.

Target Market(s)

Residential market in oslo, Norway

Industry/Entity Type

Plumbing

Coding

Coded - Design and coding required

Requirements
Must have
• Build with elementor (wordpress), SEO friendly, A good CTA for phone, mobile responsive. Fast loading time. A Clean design.
Should not have
• Stock images that look "fake". All pictures have an authentic feel.

```html
<!DOCTYPE html>
<html lang="no">
<head>
<meta charset="utf-8">
<title>Vannlinje Nord – Rørlegger i Oslo</title>
<link rel="stylesheet" href="https://fonts.googleapis.com/css2?family=Inter:wght@400;500;600;700&display=swap">
<style>
:root{
  --red:#a62c30;
  --black:#1e1e1e;
  --light:#f0f1f2;
  --white:#ffffff;
  --board:#e7e7e7;
  --muted:#6c6c6c;
  --line:#cfd0d2;
}
*{box-sizing:border-box;margin:0;padding:0}
html,body{width:1200px;height:3339px;overflow:hidden}
body{background:var(--board);font-family:"Inter",sans-serif;color:var(--black);position:relative}
.abs{position:absolute}

/* style sheet header */
.brand-mark{left:203px;top:140px;font-size:18px;font-weight:500;letter-spacing:3px}
.spec-title{font-size:28px;font-weight:400;top:98px}
.spec-fonts{left:582px}
.spec-colors{left:838px}
.spec-font-name{left:582px;top:142px;font-size:17px;color:#777}
.swatch{top:138px;width:41px;height:41px;border-radius:50%}
.swatch-label{top:186px;font-size:10px;color:#777;width:50px;text-align:center}

/* site */
.site{left:223px;top:279px;width:790px;height:2955px;background:var(--white);overflow:hidden}
.nav{left:106px;top:4px;width:578px;height:32px;background:var(--light);display:flex;align-items:center;padding:0 13px}
.nav .logo{font-size:11px;font-weight:600;letter-spacing:1.4px}
.nav ul{list-style:none;display:flex;gap:18px;margin-left:auto;margin-right:14px;font-size:7.5px;color:#444}
.round-phone{width:21px;height:21px;border-radius:50%;background:var(--red);display:flex;align-items:center;justify-content:center}
.round-phone svg{width:10px;height:10px}

.hero-bg{left:0;top:0;width:790px;height:373px;background:linear-gradient(180deg,#f7f7f7,#eceded);border-bottom-left-radius:60px}
.hero-photo{left:412px;top:84px;width:378px;height:289px;background:radial-gradient(circle at 30% 55%,#b8393c 0,#8e2a2d 22%,transparent 40%),radial-gradient(circle at 78% 45%,#a0784a 0,#6d5132 25%,transparent 45%),linear-gradient(135deg,#e9e9e9,#cfcfcf);}
.eyebrow{left:106px;top:108px;font-size:7px;color:#777}
.hero-title{left:106px;top:122px;font-size:30px;line-height:33px;font-weight:500;width:300px}

.call-btn{display:flex;align-items:center;gap:7px;height:28px;padding:0 9px 0 4px;border:1px solid #bdbdbd;border-radius:14px;background:var(--white);font-size:7.5px;font-weight:500;white-space:nowrap}
.call-btn .round-phone{width:20px;height:20px}

.quote-form{left:452px;top:333px;width:232px;height:302px;background:var(--white);box-shadow:0 6px 24px rgba(0,0,0,.07);padding:18px 25px}
.quote-form h3{font-size:8.5px;font-weight:600;margin-bottom:30px}
.quote-form label{display:block;font-size:6.5px;color:#555;margin-bottom:6px}
.field{height:28px;border-radius:14px;background:var(--white);box-shadow:0 2px 8px rgba(0,0,0,.08);font-size:6.5px;color:#888;display:flex;align-items:center;justify-content:space-between;padding:0 14px;margin-bottom:17px}
.field.area{height:43px;margin-bottom:12px}
.send-btn{height:30px;border-radius:15px;background:var(--red);color:var(--white);font-size:7.5px;font-weight:600;display:flex;align-items:center;justify-content:center;gap:5px}

.why-title{left:106px;top:430px;font-size:23px;line-height:25px;font-weight:500}
.checks{left:106px;top:496px;width:300px;display:grid;grid-template-columns:148px 148px;row-gap:12px;font-size:7.5px;color:#444}
.checks li{list-style:none;display:flex;align-items:center;gap:6px}
.checks svg{width:9px;height:9px;flex:none}

.panel{background:var(--light);border-radius:60px 60px 0 60px}
.about{left:0;top:691px;width:790px;height:342px;border-radius:60px 60px 0 60px}
.team-photo{left:106px;top:787px;width:242px;height:179px;background:linear-gradient(180deg,#fafafa 0,#eeeeee 40%,#2a2a2a 41%,#1d1d1d 100%)}
.about-title{left:434px;top:746px;font-size:23px;line-height:25px;font-weight:500;width:270px}
.about-text{left:434px;top:837px;width:225px;font-size:7px;line-height:13px;color:#666}
.about-text p+p{margin-top:10px}

.section-title{font-size:23px;font-weight:500}
.services-title{left:0;width:790px;top:1084px;text-align:center}
.services{left:106px;top:1135px;width:578px;display:flex;justify-content:space-between}
.service{width:84px;height:85px;background:var(--light);display:flex;flex-direction:column;align-items:center;justify-content:center;gap:8px;font-size:7px;color:#444}
.service .icon{width:26px;height:26px;border-radius:4px;background:linear-gradient(135deg,#c9c9c9,#a62c30)}

.contact{left:0;top:1274px;width:790px;height:335px}
.van-photo{left:399px;top:1296px;width:391px;height:266px;background:radial-gradient(ellipse at 55% 55%,#262626 0,#1b1b1b 38%,transparent 60%),linear-gradient(180deg,#e4e5e7,#f2f2f3)}
.contact-title{left:106px;top:1369px;font-size:23px;line-height:25px;font-weight:500}
.contact-text{left:106px;top:1437px;width:200px;font-size:7px;line-height:13px;color:#666}

.projects-title{left:106px;top:1664px}
.project{top:1713px;width:183px}
.project .img{height:254px}
.project .cap{display:flex;justify-content:space-between;font-size:7px;color:#666;margin-top:8px}

.faq{left:0;top:2039px;width:790px;height:316px}
.faq-title{left:0;width:790px;top:2088px;text-align:center;line-height:26px}
.faq-item{width:233px;border-bottom:1px solid #9a9a9a;display:flex;justify-content:space-between;gap:10px;font-size:7px;line-height:11px;color:#555;padding-bottom:6px}
.faq-item span:last-child{font-size:10px}

.reviews-title{left:106px;top:2406px}
.review{top:2458px;width:183px;height:182px;background:var(--light);padding:25px 25px}
.stars{color:#f2a900;font-size:8px;letter-spacing:1px}
.review p{font-size:6.5px;line-height:13px;color:#555;margin-top:8px;height:80px}
.review .who{font-size:6.5px;font-weight:600;margin-top:20px}
.dots{left:0;width:790px;top:2663px;display:flex;justify-content:center;gap:4px}
.dots i{width:5px;height:5px;border-radius:50%;border:1px solid var(--red)}
.dots i.on{background:var(--red)}

.badges{left:106px;top:2725px;width:578px;display:flex;justify-content:space-between;align-items:center}
.badge{width:34px;height:30px;background:#d5d6d8;border-radius:4px}
.badge.round{border-radius:50%;width:30px}
.badge.wide{width:80px;height:26px}

.footer{left:0;top:2812px;width:790px;height:143px;background:var(--light);border-top-left-radius:60px}
.foot-addr{left:106px;top:2861px;font-size:7px;line-height:15px;color:#444}
.foot-logo{left:0;width:790px;top:2862px;text-align:center;font-size:11px;font-weight:600;letter-spacing:1.4px}
.foot-links{left:0;width:790px;top:2889px;display:flex;justify-content:center;gap:0;font-size:7px;color:#555}
.foot-links span{padding:0 10px;border-left:1px solid #999;line-height:9px}
.foot-links span:first-child{border-left:none}
.foot-social{left:662px;top:2864px;display:flex;gap:6px}
.foot-social i{width:8px;height:8px;border-radius:50%;background:#888}
.foot-copy{left:655px;top:2889px;font-size:7px;color:#555}
</style>
</head>
<body>

<svg width="0" height="0" style="position:absolute">
  <defs>
    <symbol id="phone" viewBox="0 0 24 24"><path fill="#fff" d="M6.6 10.8a15.1 15.1 0 0 0 6.6 6.6l2.2-2.2c.3-.3.7-.4 1-.2 1.1.4 2.3.6 3.6.6.6 0 1 .4 1 1V20c0 .6-.4 1-1 1A17 17 0 0 1 3 4c0-.6.4-1 1-1h3.5c.6 0 1 .4 1 1 0 1.3.2 2.5.6 3.6.1.3 0 .7-.2 1z"/></symbol>
    <symbol id="tick" viewBox="0 0 12 12"><circle cx="6" cy="6" r="5" fill="none" stroke="#a62c30" stroke-width="1.2"/><path d="M3.6 6.2l1.7 1.6 3.1-3.3" fill="none" stroke="#a62c30" stroke-width="1.2"/></symbol>
  </defs>
</svg>

<!-- Style sheet -->
<div class="abs brand-mark">VANNLINJE NORD</div>
<div class="abs spec-title spec-fonts">Fonts:</div>
<div class="abs spec-font-name">Inter</div>
<div class="abs spec-title spec-colors">Colors:</div>
<div class="abs swatch" style="left:839px;background:var(--red)"></div>
<div class="abs swatch" style="left:891px;background:var(--black)"></div>
<div class="abs swatch" style="left:942px;background:var(--light)"></div>
<div class="abs swatch" style="left:993px;background:var(--white)"></div>
<div class="abs swatch-label" style="left:834px">#a62c30</div>
<div class="abs swatch-label" style="left:886px">#1e1e1e</div>
<div class="abs swatch-label" style="left:937px">#f0f1f2</div>
<div class="abs swatch-label" style="left:988px">#ffffff</div>

<!-- Website -->
<main class="abs site">

  <div class="abs hero-bg"></div>
  <div class="abs hero-photo" role="img" aria-label="Photo of a red pipe wrench and brass pipe fittings on a wet surface"></div>

  <nav class="abs nav">
    <span class="logo">VANNLINJE NORD</span>
    <ul><li>Hjem</li><li>Tjenester</li><li>Om Oss</li><li>Miljø Og Kvalitet</li><li>Kontakt</li></ul>
    <span class="round-phone"><svg><use href="#phone"/></svg></span>
  </nav>

  <div class="abs eyebrow">Bekkestad Rør AS – Vannlinje Nord</div>
  <h1 class="abs hero-title">Vi Hjelper deg Med alt Arbeid Relatert til Rørlegging</h1>
  <a class="abs call-btn" style="left:106px;top:243px"><span class="round-phone"><svg><use href="#phone"/></svg></span>Ring Nå 23 86 51 94</a>

  <form class="abs quote-form">
    <h3>Fyll Ut Uforpliktende Skjema, Få Svar Idag!</h3>
    <label>Hvilket område ønsker du hjelp i?</label>
    <div class="field">Velge <span>⌄</span></div>
    <label>Hva for type av arbeid?</label>
    <div class="field">Velge <span>⌄</span></div>
    <label>Skriv en kort melding/beskrivelse:</label>
    <div class="field area"></div>
    <div class="send-btn">Send Inn Forespørselen Din <span>➤</span></div>
  </form>

  <h2 class="abs why-title">Hvorfor velge Vannlinje<br>Nord?</h2>
  <ul class="abs checks">
    <li><svg><use href="#tick"/></svg>Uforpliktende og rimelige priser</li>
    <li><svg><use href="#tick"/></svg>Alltid fastpris</li>
    <li><svg><use href="#tick"/></svg>Punktlig ankomst</li>
    <li><svg><use href="#tick"/></svg>Kun sertifiserte og</li>
    <li><svg><use href="#tick"/></svg>Konkurransedyktige priser</li>
    <li><svg><use href="#tick"/></svg>Jobben utført riktig</li>
  </ul>

  <section class="abs panel about"></section>
  <div class="abs team-photo" role="img" aria-label="Photo of two plumbers in dark company sweaters"></div>
  <h2 class="abs about-title">Vi er et Godt Alternativ når Du ønsker Hjelp med Rørlegging</h2>
  <div class="abs about-text">
    <p>I flere år har huseiere og bedrifter i hele Oslo regnet med at Vannlinje Nord for å tilby profesjonelle rørleggingstjenester. Vi er stolte når det gjelder erfaring, tilgjengelighet og overkommelig pris!</p>
    <p>Mange år i bransjen har gitt oss erfaringen du trenger for å få et vellykket resultat.</p>
  </div>
  <a class="abs call-btn" style="left:434px;top:949px"><span class="round-phone"><svg><use href="#phone"/></svg></span>Ring Nå 23 86 51 94</a>

  <h2 class="abs section-title services-title">Noen Få Utvalgte Tjenester</h2>
  <div class="abs services">
    <div class="service"><span class="icon" role="img" aria-label="Bathroom icon"></span>Våtrom</div>
    <div class="service"><span class="icon" role="img" aria-label="Drain sealing icon"></span>Tette avløpsrør</div>
    <div class="service"><span class="icon" role="img" aria-label="Heat pump icon"></span>Varmepumper</div>
    <div class="service"><span class="icon" role="img" aria-label="Water leak icon"></span>Vannlekkasje</div>
    <div class="service"><span class="icon" role="img" aria-label="On-call plumber icon"></span>Rørleggervakt</div>
    <div class="service"><span class="icon" role="img" aria-label="Emergency help icon"></span>Akutthjelp</div>
  </div>

  <section class="abs panel contact"></section>
  <div class="abs van-photo" role="img" aria-label="Photo of the company's black service van with red stripe"></div>
  <h2 class="abs contact-title">Ta Kontakt for en<br>Uforpliktende Prat</h2>
  <p class="abs contact-text">Du kan benytte deg av denne typen tjenester både for boliger og for næringsbygg.</p>
  <a class="abs call-btn" style="left:106px;top:1482px"><span class="round-phone"><svg><use href="#phone"/></svg></span>Ring Nå 23 86 51 94</a>

  <h2 class="abs section-title projects-title">Nylig Utførte Prosjekter</h2>
  <div class="abs project" style="left:106px"><div class="img" role="img" aria-label="Photo of a grey bathroom with double basins and bathtub" style="background:linear-gradient(160deg,#6d6d6d,#3a3a3a 60%,#8a8a8a)"></div><div class="cap"><span>Project Name</span><span>+</span></div></div>
  <div class="abs project" style="left:304px"><div class="img" role="img" aria-label="Photo of a dark tiled shower with wall-hung toilet" style="background:linear-gradient(90deg,#3b3b3b 55%,#7a7a7a 55%,#9a9a9a)"></div><div class="cap"><span>Project Name</span><span>+</span></div></div>
  <div class="abs project" style="left:501px"><div class="img" role="img" aria-label="Photo of a bathroom with wood panelling and glass shower" style="background:linear-gradient(180deg,#4a4a4a,#8c8c8c 40%,#5a5a5a)"></div><div class="cap"><span>Project Name</span><span>+</span></div></div>
  <div class="abs project" style="left:699px"><div class="img" role="img" aria-label="Photo of a light grey bathroom vanity" style="background:linear-gradient(180deg,#a5a5a5,#7b7b7b)"></div><div class="cap"><span>Project Name</span><span>+</span></div></div>

  <section class="abs panel faq"></section>
  <h2 class="abs section-title faq-title">Vår Rørleggerfirma i Oslo Tilbyr God<br>og Rimelig Rørleggerhjelp</h2>
  <div class="abs faq-item" style="left:154px;top:2172px"><span>Hvilke tjenester tilbyr dere?</span><span>+</span></div>
  <div class="abs faq-item" style="left:402px;top:2172px"><span>Hvilke tider jobber dere?</span><span>+</span></div>
  <div class="abs faq-item" style="left:154px;top:2208px"><span>Ønsker du rørlegger til installasjon eller reparasjon av avløp eller skader etter lekkasjer?</span><span>+</span></div>
  <div class="abs faq-item" style="left:402px;top:2208px"><span>Trenger du rørlegger til oppussing eller rehabilitering av f.eks. bad og toalett?</span><span>+</span></div>
  <a class="abs call-btn" style="left:340px;top:2271px"><span class="round-phone"><svg><use href="#phone"/></svg></span>Ring Nå 23 86 51 94</a>

  <h2 class="abs section-title reviews-title">Lang Erfaring du kan Stole På</h2>
  <div class="abs review" style="left:-92px"><div class="stars">★★★★★</div><p>Bekkestad Rør AS var svært raske til å respondere på jobboppdraget. Fornøyd med jobbutførelsen.</p><div class="who">Arne Moland</div></div>
  <div class="abs review" style="left:106px"><div class="stars">★★★★★</div><p>Bekkestad Rør AS gjorde jobben på en utmerket måte. De sendte en hyggelig og flink rørlegger som var på plass innen 20 minutter. Anbefales.</p><div class="who">Ingrid Hals</div></div>
  <div class="abs review" style="left:304px"><div class="stars">★★★★★</div><p>Kom til avtalt tid, utførte jobben på en god profesjonell måte. Oppdaget også om andre problemer som burde fikses. Fornøyd.</p><div class="who">Eirik Sandvold</div></div>
  <div class="abs review" style="left:501px"><div class="stars">★★★★★</div><p>Bekkestad Rør AS var svært raske til å respondere på jobboppdraget. Fornøyd med jobbutførelsen. Hyggelige folk.</p><div class="who">Arne Moland</div></div>
  <div class="abs review" style="left:699px"><div class="stars">★★★★★</div><p>Bekkestad Rør AS var svært raske til å respondere på jobboppdraget. Fornøyd med jobbutførelsen. Hyggelige folk.</p><div class="who">Arne Moland</div></div>
  <div class="abs dots"><i></i><i class="on"></i><i></i></div>

  <div class="abs badges">
    <span class="badge wide"></span>
    <span class="badge wide"></span>
    <span class="badge round"></span>
    <span class="badge wide"></span>
    <span class="badge"></span>
    <span class="badge"></span>
  </div>

  <footer class="abs footer"></footer>
  <div class="abs foot-addr">Fjordveien 14, 0561 Oslo<br>23 86 51 94<br>org nr 912 447 305</div>
  <div class="abs foot-logo">VANNLINJE NORD</div>
  <div class="abs foot-links"><span>Hjem</span><span>Tjenester</span><span>Om Oss</span><span>Miljø Og Kvalitet</span><span>Kontakt</span></div>
  <div class="abs foot-social"><i></i><i></i></div>
  <div class="abs foot-copy">© 2023</div>

</main>
</body>
</html>
```